Business Card Design Project

I am seeking a business card for my life coaching career. I specialize in coaching executives and entrepreneurs. Consciousness plays a key role in my practice.
Updates

I would like to see different fonts -I don't like the way the capital J looks. I only want my name once on the card, on the front. I like everything centered on the front, with a white background, grey and green on the front; and the same grey on the back with bullet points next to each quality; centered. I like a subtle shadow of the mountains behind the text on the back of the card. I don't want the mountains on either side to be too big. Thank you.

Target Market(s)

Middle age business owners/executives

Industry/Entity Type

Business

Contact Information for Business Card

The front design is my name and a mountain logo. I want to have my name prominently shown.

Requirements
Must have
• Front of card:
• My name prominent sized font
• Helping clients lead more fulfilling lives;
• Executive Life Coach
• 555-304-7781
• rkovet4@mailbriar.com
• Back of Card:
• Providing Unparalleled support
• Providing a safe place to grow in self-awareness
• 20+ years entrepreneurial experience
• Trust
• Integrity
Nice to have
• Easy to read font; warm colors reflecting a masculine personality.

Files

```html
<!DOCTYPE html>
<html lang="en">
<head>
<meta charset="utf-8">
<title>Miles Harlan – Business Card</title>
<link rel="stylesheet" href="https://fonts.googleapis.com/css2?family=Montserrat:wght@700&family=Josefin+Sans:wght@300;400&display=swap">
<style>
  :root {
    --backdrop: #cfd8e0;
    --card-white: #f4f4f6;
    --card-dark: #3b3838;
    --forest: #566b3a;
    --charcoal: #3d3a3b;
    --mist: #b9b5b4;
  }
  html, body {
    margin: 0;
    width: 1200px;
    height: 898px;
    overflow: hidden;
    background: var(--backdrop);
  }
  .canvas {
    position: relative;
    width: 1200px;
    height: 898px;
  }
  .card {
    position: absolute;
    top: 289px;
    width: 560px;
    height: 320px;
    box-sizing: border-box;
    display: flex;
    flex-direction: column;
    align-items: center;
  }
  .card--front {
    left: 20px;
    background: var(--card-white);
    color: var(--charcoal);
    padding-top: 52px;
  }
  .card--back {
    left: 620px;
    background: var(--card-dark);
    color: var(--mist);
    justify-content: center;
  }
  .brand-dot {
    width: 34px;
    height: 34px;
    border-radius: 50%;
    background: var(--forest);
    margin-bottom: 18px;
  }
  .name {
    font-family: "Montserrat", sans-serif;
    font-weight: 700;
    font-size: 56px;
    line-height: 1;
    letter-spacing: 1px;
    color: var(--forest);
    margin: 0;
  }
  .tagline {
    font-family: "Josefin Sans", sans-serif;
    font-weight: 300;
    font-size: 17.5px;
    letter-spacing: 0.5px;
    text-transform: uppercase;
    margin: 10px 0 22px;
  }
  .role {
    font-family: "Montserrat", sans-serif;
    font-weight: 700;
    font-size: 17px;
    text-transform: uppercase;
    margin: 0 0 8px;
  }
  .contact {
    font-family: "Josefin Sans", sans-serif;
    font-weight: 400;
    font-size: 17px;
    text-transform: uppercase;
    line-height: 1.55;
    text-align: center;
    margin: 0;
  }
  .qualities {
    list-style: none;
    margin: 0;
    padding: 0;
    font-family: "Josefin Sans", sans-serif;
    font-weight: 300;
    font-size: 16px;
    letter-spacing: 0.5px;
    text-transform: uppercase;
    line-height: 1.75;
    text-align: center;
  }
  .qualities li::before {
    content: "\274B";
    font-size: 11px;
    margin-right: 6px;
    vertical-align: 2px;
  }
</style>
</head>
<body>
<main class="canvas">
  <section class="card card--front">
    <div class="brand-dot" aria-hidden="true"></div>
    <h1 class="name">MILES HARLAN</h1>
    <p class="tagline">Helping clients lead more fulfilling lives</p>
    <p class="role">Executive Life Coach</p>
    <p class="contact">555-304-7781<br>rkovet4@mailbriar.com</p>
  </section>
  <section class="card card--back">
    <ul class="qualities">
      <li>Providing unparalleled support</li>
      <li>A safe place to grow in self-awareness</li>
      <li>20+ years entrepreneurial experience</li>
      <li>Trust</li>
      <li>Integrity</li>
    </ul>
  </section>
</main>
</body>
</html>
```